Postcard flyer for body postive dance classes

We need an eye catching double sided A6 postcard for body positive dance classes. The business name is stepbloomjoy and already have a rough logo and some text that needs tidying up and putting together. The design needs to be simple and elegant. We are appealing to a diverse range of adult women with or without dance experience to join us in a safe, supportive and creative environment. We would like the design to use black, white and a soft green. The final design should communicate movement, contentment and wholeness. File with information attached.

Target Market(s)

Diverse range of adult women

Industry/Entity Type

Health And Wellness

Font styles to use
Other font styles liked:
• Candara or similar but open to suggestions

Colors
abd036
cadf82
eaf2ce
fffefb
fef9ed
fff3d1
ffffff

Requirements
Must have
• Logo and text provided.
Nice to have
• Sense of movement. Match to website colours and style.
Should not have
• Intimidating perfect body images

```html
<!DOCTYPE html>
<html lang="en">
<head>
<meta charset="utf-8">
<title>stepbloomjoy postcard</title>
<link href="https://fonts.googleapis.com/css2?family=Cabin:wght@400;500;600;700&display=swap" rel="stylesheet">
<style>
  :root {
    --green: #4db848;
    --green-soft: #abd036;
    --green-pale: #cadf82;
    --ink: #1c1c1c;
    --text: #2b2b2b;
    --grey: #bdbdbd;
    --grey-light: #e4e4e4;
    --paper: #ffffff;
    --backdrop: #f3f3f1;
  }
  * { margin: 0; padding: 0; box-sizing: border-box; }
  html, body { width: 1200px; height: 1200px; overflow: hidden; }
  body {
    background: var(--backdrop);
    font-family: Candara, "Cabin", sans-serif;
    color: var(--text);
    position: relative;
  }
  .card {
    position: absolute;
    left: 210px;
    width: 780px;
    height: 560px;
    background: var(--paper);
    overflow: hidden;
  }
  .card--front { top: 26px; }
  .card--back { top: 614px; }
  .card svg.art { position: absolute; inset: 0; width: 780px; height: 560px; }

  /* front */
  .wordmark {
    position: absolute; left: 292px; top: 262px;
    font-size: 66px; font-weight: 400; color: #333333; letter-spacing: 0.5px;
  }
  .front-url {
    position: absolute; left: 398px; top: 337px;
    font-size: 17px; color: var(--text);
    border-top: 1px solid #9a9a9a; border-bottom: 1px solid #9a9a9a;
    padding: 2px 2px 3px;
  }
  .badge {
    position: absolute; left: 108px; top: 372px;
    width: 126px; height: 126px; border-radius: 50%;
    border: 2px solid #d0d0d0; background: var(--paper);
    display: flex; align-items: center; justify-content: center;
    font-size: 17px; font-weight: 600; color: var(--ink);
  }
  .tagline {
    position: absolute; font-weight: 700; color: var(--ink);
    border-top: 1px solid #999; border-bottom: 1px solid #999;
    white-space: nowrap;
  }
  .tagline .dot { color: var(--green); padding: 0 4px; }
  .tagline--front { left: 24px; top: 508px; font-size: 16px; padding: 3px 6px; }

  /* back */
  .headline {
    position: absolute; left: 43px; top: 22px; width: 290px; text-align: center;
    font-size: 30px; font-weight: 600; color: var(--green); line-height: 1.1;
  }
  .subhead {
    position: absolute; left: 43px; top: 56px;
    font-size: 24px; font-weight: 400; color: var(--ink);
  }
  .body-copy {
    position: absolute; left: 43px; top: 102px; width: 300px;
    font-size: 14.5px; line-height: 19px; color: var(--text);
  }
  .body-copy p + p { margin-top: 9px; }
  .contact-title {
    position: absolute; left: 43px; top: 260px;
    font-size: 22px; font-weight: 600; color: var(--green);
  }
  .contact-list {
    position: absolute; left: 43px; top: 291px; list-style: none;
    font-size: 14.5px; line-height: 19px;
  }
  .contact-list li { display: flex; align-items: center; gap: 5px; }
  .contact-list svg { width: 10px; height: 10px; fill: var(--green); flex: none; }
  .badge--small {
    left: 472px; top: 22px; width: 72px; height: 72px;
    font-size: 10px; border-width: 2px;
  }
  .tagline--back { left: 426px; top: 101px; font-size: 9px; padding: 1px 3px; }
</style>
</head>
<body>

<section class="card card--front">
  <svg class="art" viewBox="0 0 780 560">
    <ellipse role="img" aria-label="Faint grey floral swirl pattern" cx="80" cy="280" rx="110" ry="140" fill="#f2f2f2"/>
    <ellipse role="img" aria-label="Faint green floral swirl pattern" cx="700" cy="120" rx="90" ry="110" fill="#eef5dc"/>
    <path d="M0 150 C60 95 160 55 260 50 C170 70 80 120 0 175 Z" fill="var(--grey-light)"/>
    <path d="M0 165 C70 110 170 55 250 48 C160 75 70 135 0 190 Z" fill="var(--green)"/>
    <path d="M380 95 C500 150 640 140 780 100 L780 125 C640 160 490 160 380 95 Z" fill="var(--grey-light)"/>
    <path d="M420 110 C540 170 660 160 780 130 L780 180 C650 190 520 170 420 110 Z" fill="var(--green)"/>
    <path role="img" aria-label="Photo of a woman in a black bodysuit leaping joyfully" d="M180 5 L340 5 L405 115 L385 250 L280 258 L262 350 L150 362 L125 250 Z" fill="url(#photoFront)"/>
    <path d="M0 360 C120 320 260 340 420 400 C560 450 680 420 780 360 L780 380 C670 450 540 470 410 420 C260 360 120 345 0 380 Z" fill="var(--grey-light)"/>
    <path d="M0 380 C130 330 260 340 380 410 C500 470 620 470 780 320 L780 340 C640 480 500 500 370 430 C250 365 130 355 0 400 Z" fill="var(--paper)"/>
    <path d="M560 430 C650 410 720 350 780 280 L780 310 C720 380 650 430 560 430 Z" fill="var(--green)"/>
    <path d="M200 390 C300 460 420 510 520 505 C630 500 710 450 780 380 L780 395 C710 470 620 515 520 520 C420 520 310 470 200 390 Z" fill="var(--ink)"/>
    <defs>
      <linearGradient id="photoFront" x1="0" y1="0" x2="1" y2="1">
        <stop offset="0" stop-color="#d9d9d9"/>
        <stop offset="1" stop-color="#3a3a3a"/>
      </linearGradient>
    </defs>
  </svg>
  <div class="wordmark">stepbloomjoy</div>
  <div class="front-url">www.stepbloomjoy.com.au</div>
  <div class="badge">stepbloomjoy</div>
  <div class="tagline tagline--front">Movement<span class="dot">•</span>Contentment<span class="dot">•</span>Wholeness</div>
</section>

<section class="card card--back">
  <svg class="art" viewBox="0 0 780 560">
    <ellipse role="img" aria-label="Faint grey floral swirl pattern" cx="60" cy="470" rx="90" ry="90" fill="#efefef"/>
    <ellipse role="img" aria-label="Light green swirl ornament" cx="370" cy="370" rx="40" ry="80" fill="#eef5dc"/>
    <path d="M0 530 C150 500 280 500 390 540 L390 560 L0 560 Z" fill="var(--grey-light)"/>
    <path d="M0 545 C140 515 280 515 390 550 L390 560 L0 560 Z" fill="#9e9e9e"/>
    <path d="M372 0 C420 90 420 190 360 290 C300 380 300 470 400 560 L380 560 C270 470 280 370 340 280 C390 190 395 90 355 0 Z" fill="var(--green)"/>
    <path role="img" aria-label="Photo of a dancer in black arching backwards mid-leap" d="M255 335 L320 330 L315 400 L290 480 L220 530 L160 520 L165 430 L235 385 Z" fill="url(#photoBack)"/>
    <rect x="642" y="33" width="88" height="88" fill="var(--grey-light)"/>
    <rect x="426" y="294" width="304" height="124" fill="var(--grey-light)"/>
    <defs>
      <linearGradient id="photoBack" x1="0" y1="0" x2="1" y2="1">
        <stop offset="0" stop-color="#cfcfcf"/>
        <stop offset="1" stop-color="#333"/>
      </linearGradient>
    </defs>
  </svg>

  <h1 class="headline">Flow with life</h1>
  <h2 class="subhead">through your inner dancer</h2>
  <div class="body-copy">
    <p>Dance is joy, dance is love. Dance is at the core of our being, a celebration of movement, vitality and wholeness.</p>
    <p>If you’ve never danced before and always wanted to or you want to reignite your past love of dance, join us at stepbloomjoy to start your journey.</p>
  </div>
  <div class="contact-title">Contact US</div>
  <ul class="contact-list">
    <li><svg viewBox="0 0 10 10"><path d="M2 0 L4 2.5 L3 3.6 C3.6 5 5 6.4 6.4 7 L7.5 6 L10 8 L8.5 10 C4 9.5 0.5 6 0 1.5 Z"/></svg>0400517286</li>
    <li><svg viewBox="0 0 10 10"><path d="M0 2 H10 V8.5 H0 Z M0.8 2.6 L5 5.8 L9.2 2.6" stroke="#fff" stroke-width="0.8"/></svg>mara@stepbloomjoy.com.au</li>
    <li><svg viewBox="0 0 10 10"><circle cx="5" cy="5" r="4.6"/></svg>www.stepbloomjoy.com.au</li>
    <li><svg viewBox="0 0 10 10"><path d="M5 0 C2.5 0 1.2 1.8 1.2 3.6 C1.2 6 5 10 5 10 C5 10 8.8 6 8.8 3.6 C8.8 1.8 7.5 0 5 0 Z"/></svg>Northvale/Eastbrook</li>
  </ul>

  <div class="badge badge--small">stepbloomjoy</div>
  <div class="tagline tagline--back">Movement<span class="dot">•</span>Contentment<span class="dot">•</span>Wholeness</div>
</section>

</body>
</html>
```